Modern Dental Appointment Reminder/Business Card

We already have a beautiful logo and icon picked from here on PixelHarbor, now we need someone to make them into a beautiful business card for us! This business card will also function as an appointment reminder card for patients. It will be double sided and must include:
Front
-Contact Info as Follows:
(Gavin T Morrow, DDS
Family and Cosmetic Dentistry
2947 S 3260 E Ste 400
Cedar Vale, Nevada 89093)
-Our Logo or Icon (your choice, if Icon must write "Bluefern Dental" below it like in the example file)
Back
-"You're Invited!"
-"Your next appointment is on"
-Place to write date & time
-"Please call 24hrs ahead if appointment is to be cancelled
-Our Icon

Logo and Icon to be used are attached below, along with an example of what we need.
Please do NOT use lots of red! We want the red to just be an accent. Please use grey, white, or even a muted teal for the majority of the card.

Industry/Entity Type

Dentistry

Contact Information for Business Card

Gavin T Morrow, DDS
2947 S 3260 E Ste 400
Cedar Vale, Nevada 89093

Colors
cfeae6

Requirements
Should not have
• Lots of red!

```html
<!DOCTYPE html>
<html lang="en">
<head>
<meta charset="utf-8">
<title>Bluefern Dental – Business &amp; Appointment Card</title>
<link rel="stylesheet" href="https://fonts.googleapis.com/css2?family=Libre+Baskerville:wght@400;700&family=Arimo:wght@400&display=swap">
<style>
  :root {
    --bg: #e9eceb;
    --card: #ffffff;
    --accent-red: #a3202a;
    --charcoal: #4a4843;
    --text-grey: #555555;
    --label-grey: #9a9a9a;
    --rule: #c8c8c8;
  }
  html, body {
    margin: 0;
    width: 1200px;
    height: 1108px;
    overflow: hidden;
    background: var(--bg);
  }
  .sheet {
    position: relative;
    width: 1200px;
    height: 1108px;
    display: flex;
    justify-content: center;
    align-items: center;
    gap: 60px;
  }
  .card {
    position: relative;
    width: 420px;
    height: 720px;
    background: var(--card);
    border-radius: 26px;
    box-shadow: 0 10px 30px rgba(0,0,0,0.12);
    display: flex;
    flex-direction: column;
    align-items: center;
    box-sizing: border-box;
  }

  /* Front */
  .card--front { padding-top: 110px; }
  .brand-mark {
    width: 150px;
    height: 150px;
    border-radius: 50%;
    background: var(--charcoal);
  }
  .brand-name {
    margin-top: 28px;
    font-family: "Libre Baskerville", serif;
    font-weight: 400;
    font-size: 38px;
    letter-spacing: 1px;
    color: var(--accent-red);
    text-align: center;
    line-height: 1.15;
    text-transform: uppercase;
  }
  .contact { margin-top: 110px; text-align: center; }
  .contact__name {
    font-family: "Libre Baskerville", serif;
    font-weight: 700;
    font-size: 24px;
    color: var(--accent-red);
    text-transform: uppercase;
  }
  .contact__title {
    font-family: "Libre Baskerville", serif;
    font-weight: 400;
    color: var(--text-grey);
    font-size: 20px;
    margin-left: 6px;
  }
  .contact__specialty {
    font-family: "Arimo", sans-serif;
    font-size: 20px;
    color: var(--text-grey);
    margin-top: 6px;
  }
  .contact__rule {
    width: 200px;
    height: 1px;
    margin: 20px auto 18px;
    background: linear-gradient(to right, transparent, #888, transparent);
  }
  .contact__address {
    font-family: "Arimo", sans-serif;
    font-size: 20px;
    line-height: 1.35;
    color: var(--text-grey);
  }

  /* Back */
  .card--back { padding-top: 200px; }
  .icon-mark {
    width: 72px;
    height: 72px;
    border-radius: 50%;
    background: var(--charcoal);
  }
  .invite__headline {
    margin-top: 22px;
    font-family: "Libre Baskerville", serif;
    font-weight: 700;
    font-size: 30px;
    color: var(--accent-red);
    text-transform: uppercase;
  }
  .invite__lead {
    margin-top: 4px;
    font-family: "Libre Baskerville", serif;
    font-size: 21px;
    color: var(--text-grey);
  }
  .write-field {
    width: 280px;
    margin-top: 36px;
    border-bottom: 1px solid var(--rule);
    padding-bottom: 6px;
    font-family: "Arimo", sans-serif;
    font-size: 26px;
    color: var(--label-grey);
  }
  .write-field + .write-field { margin-top: 40px; }
  .cancel-note {
    margin-top: 56px;
    font-family: "Arimo", sans-serif;
    font-size: 16px;
    line-height: 1.3;
    color: var(--text-grey);
    text-align: center;
  }
</style>
</head>
<body>
<main class="sheet">
  <section class="card card--front" aria-label="Card front">
    <div class="brand-mark" aria-hidden="true"></div>
    <div class="brand-name">Bluefern<br>Dental</div>
    <div class="contact">
      <div><span class="contact__name">Gavin T Morrow</span><span class="contact__title">DDS</span></div>
      <div class="contact__specialty">Family and Cosmetic Dentistry</div>
      <div class="contact__rule"></div>
      <div class="contact__address">2947 S 3260 E Ste 400<br>Cedar Vale, Nevada 89093</div>
    </div>
  </section>

  <section class="card card--back" aria-label="Card back">
    <div class="icon-mark" aria-hidden="true"></div>
    <div class="invite__headline">You're Invited!</div>
    <div class="invite__lead">Your next appointment is on</div>
    <div class="write-field">TIME</div>
    <div class="write-field">DATE</div>
    <p class="cancel-note">Please call 24hrs ahead if<br>appointment is to be cancelled</p>
  </section>
</main>
</body>
</html>
```